Business Cards

The name of our firm is "Tallpine Insurance adjusters"
We separate ourselves from all other public adjusters because most of us worked for the insurance companies so we understand their games.
As Insurance adjusters we represent the Insured, not the insurance companies. Our # 1 priority is to handle the entire claim process as seamless as possible on behalf of the homeowner/business owner so they don't have to deal with the hassles and headaches. Just as the logo your team designed, I want the cards to stand out from everyone elses. I also want the cards to help better understand our services and Value on hiring us and value that we can offer.
I uploaded the logo whenever I created the project. I don't see an option on re uploading the logo anywhere. Any advise??

```html
<!DOCTYPE html>
<html lang="en">
<head>
<meta charset="utf-8">
<title>Tallpine Insurance Adjusters — Business Cards</title>
<link rel="stylesheet" href="https://fonts.googleapis.com/css2?family=Source+Sans+3:wght@400;600;700&display=swap">
<style>
  :root {
    --page-bg: #e4e4e4;
    --card-navy: #08476c;
    --card-light: #f4f4f4;
    --brand-blue: #0f5a88;
    --brand-mark: #2a6f9c;
    --front-mark: #1d5c84;
    --text-white: #ffffff;
    --text-body: #3b3b3b;
    --icon-blue: #1a6a9a;
  }
  * { margin: 0; padding: 0; box-sizing: border-box; }
  html, body { width: 1200px; height: 960px; overflow: hidden; }
  body {
    background: var(--page-bg);
    font-family: "Source Sans 3", "Source Sans Pro", Arial, sans-serif;
    position: relative;
  }
  .card {
    position: absolute;
    left: 301px;
    width: 597px;
    height: 340px;
    overflow: hidden;
  }
  .card--front {
    top: 119px;
    background: var(--card-navy);
    display: flex;
    align-items: center;
    justify-content: center;
  }
  .front-name {
    color: var(--front-mark);
    font-weight: 700;
    font-size: 40px;
    letter-spacing: 2px;
    text-transform: uppercase;
    text-align: center;
    line-height: 1.05;
  }
  .front-name small { display: block; font-size: 18px; letter-spacing: 3px; }

  .card--back { top: 512px; background: var(--card-light); }
  .back-band {
    position: absolute; left: 0; top: 0;
    width: 100%; height: 162px;
    background: var(--card-navy);
  }
  .brand-circle {
    position: absolute;
    left: 106px; top: 78px;
    width: 110px; height: 110px;
    border-radius: 50%;
    background: var(--brand-mark);
    border: 5px solid var(--card-light);
  }
  .brand-name {
    position: absolute;
    left: 61px; top: 198px;
    width: 200px;
    text-align: center;
    color: var(--brand-blue);
    font-weight: 700;
    font-size: 31px;
    line-height: 1;
    letter-spacing: 0.5px;
    text-transform: uppercase;
  }
  .brand-name small { display: block; font-size: 11.5px; letter-spacing: 0.8px; margin-top: 4px; }

  .person { position: absolute; left: 328px; top: 89px; color: var(--text-white); }
  .person-name { font-weight: 700; font-size: 20px; letter-spacing: 0.4px; text-transform: uppercase; }
  .person-title { font-size: 15px; margin-top: 1px; }

  .contact-list { position: absolute; left: 327px; top: 203px; list-style: none; }
  .contact-list li {
    display: flex; align-items: center; gap: 6px;
    font-size: 15px; color: var(--text-body); height: 20px;
  }
  .contact-list svg { width: 13px; height: 13px; fill: none; stroke: var(--icon-blue); stroke-width: 1.6; }
  .contact-list strong { color: var(--brand-blue); font-weight: 700; }
</style>
</head>
<body>
  <section class="card card--front" aria-label="Card front">
    <p class="front-name">Tallpine<small>Insurance Adjusters</small></p>
  </section>

  <section class="card card--back" aria-label="Card back">
    <div class="back-band"></div>
    <div class="brand-circle"></div>
    <p class="brand-name">Tallpine<small>Insurance Adjusters</small></p>

    <div class="person">
      <p class="person-name">Elias Varga</p>
      <p class="person-title">President</p>
    </div>

    <ul class="contact-list">
      <li>
        <svg viewBox="0 0 16 16" aria-hidden="true"><path d="M3 2l3 0 1 4-2 1c1 2 2 3 4 4l1-2 4 1 0 3c0 1-1 2-2 2C7 15 1 9 1 4c0-1 1-2 2-2z"/></svg>
        321-555-0147
      </li>
      <li>
        <svg viewBox="0 0 16 16" aria-hidden="true"><rect x="1.5" y="3.5" width="13" height="9"/><path d="M1.5 3.5l6.5 5 6.5-5"/></svg>
        elias@tallpineinad.com
      </li>
      <li>
        <svg viewBox="0 0 16 16" aria-hidden="true"><circle cx="8" cy="8" r="6.5"/><ellipse cx="8" cy="8" rx="3" ry="6.5"/><path d="M1.5 8h13"/></svg>
        <span>www.<strong>tallpineinad</strong>.com</span>
      </li>
    </ul>
  </section>
</body>
</html>
```